New banner design for mortgage broker

Looking for a banner design for mortgage broking company.
- need to use logo
- need to use colours from the logo
- like to use the headshot somehow.
- use slogan ' Helping to navigate your finance journey'
- include listing our services. Home Loans, Investment Loans, First Home Buyers, Self-employed Specialist, Car loans, Past Credit issues.
- call to action to get in contact today on 1300 642 917 or www.harbourvf.com.au
- Banner size 2.4m x 0.6m

```html
<!DOCTYPE html>
<html lang="en">
<head>
<meta charset="utf-8">
<title>Harbour Vista Finance Banner</title>
<link rel="stylesheet" href="https://fonts.googleapis.com/css2?family=Montserrat:wght@500;600;700;800&display=swap">
<style>
  :root {
    --purple: #4f2783;
    --charcoal: #4a4a4c;
    --ink: #1e1e22;
    --bg-light: #f8f8f8;
    --bg-dark: #d3d3d6;
    --white: #ffffff;
    --photo-light: #e4e1dc;
    --photo-dark: #3a3f55;
  }
  * { margin: 0; padding: 0; box-sizing: border-box; }
  html, body { width: 1200px; height: 317px; overflow: hidden; background: var(--bg-light); }
  .banner {
    position: relative; width: 1200px; height: 317px; overflow: hidden;
    background: linear-gradient(100deg, var(--bg-light) 0%, #ececee 45%, var(--bg-dark) 100%);
    font-family: "Montserrat", sans-serif;
  }
  .brand {
    position: absolute; left: 19px; top: 12px;
    display: flex; align-items: center; gap: 6px;
    color: var(--purple); font-weight: 600; font-size: 15px; letter-spacing: 0.5px;
  }
  .brand-dot { width: 14px; height: 14px; border-radius: 50%; background: var(--purple); }
  .slogan { position: absolute; left: 78px; top: 0; line-height: 1; font-weight: 800; }
  .slogan span { position: absolute; left: 0; white-space: nowrap; }
  .slogan .helping { top: 78px; font-size: 58px; color: var(--purple); }
  .slogan .navigate { top: 130px; left: 3px; font-size: 40px; color: var(--charcoal); }
  .slogan .finance { top: 177px; left: 3px; font-size: 34px; color: var(--charcoal); }
  .slogan .journey { top: 212px; left: 2px; font-size: 58px; color: var(--purple); }
  .services { position: absolute; left: 450px; top: 86px; color: var(--ink); }
  .services h2 { font-size: 23px; font-weight: 700; letter-spacing: 0.3px; }
  .service-list {
    list-style: none; position: absolute; top: 36px; left: 4px;
    display: grid; grid-template-columns: 230px 240px; grid-auto-flow: column;
    grid-template-rows: repeat(3, 43px);
  }
  .service-list li {
    position: relative; padding-left: 24px; font-size: 13px; font-weight: 600;
    letter-spacing: 0.3px; white-space: nowrap;
  }
  .service-list li::before {
    content: ""; position: absolute; left: 0; top: 3px;
    width: 6px; height: 6px; border-radius: 50%; background: var(--ink);
  }
  .portrait { position: absolute; left: 910px; top: 28px; width: 250px; height: 250px; }
  .portrait-photo {
    position: absolute; left: 9px; top: 8px; width: 222px; height: 226px; border-radius: 50%;
    background: radial-gradient(circle at 50% 35%, var(--photo-light) 0%, #cfc6b8 45%, var(--photo-dark) 100%);
  }
  .cta-bar { position: absolute; left: 0; top: 289px; width: 1200px; height: 28px; }
  .cta-text {
    position: absolute; top: 289px; height: 28px; line-height: 28px;
    color: var(--white); font-weight: 700; white-space: nowrap;
  }
  .cta-phone { left: 595px; font-size: 14px; letter-spacing: 0.3px; }
  .cta-phone .number { margin-left: 22px; }
  .cta-web { left: 926px; font-size: 13px; letter-spacing: 3.2px; }
</style>
</head>
<body>
  <div class="banner">
    <div class="brand"><span class="brand-dot"></span>Harbour Vista Finance</div>

    <h1 class="slogan">
      <span class="helping">HELPING</span>
      <span class="navigate">TO NAVIGATE</span>
      <span class="finance">YOUR FINANCE</span>
      <span class="journey">JOURNEY</span>
    </h1>

    <section class="services">
      <h2>OUR SERVICES</h2>
      <ul class="service-list">
        <li>Home Loans</li>
        <li>Investment Loans</li>
        <li>First Home Buyers</li>
        <li>Self-employed Specialist</li>
        <li>Car loans</li>
        <li>Past Credit issues</li>
      </ul>
    </section>

    <div class="portrait">
      <svg width="250" height="250" viewBox="0 0 250 250" aria-hidden="true">
        <circle cx="132" cy="122" r="121" fill="var(--purple)"/>
        <circle cx="120" cy="121" r="118" fill="#d9d9dc"/>
      </svg>
      <div class="portrait-photo" role="img" aria-label="Headshot of the mortgage broker"></div>
    </div>

    <svg class="cta-bar" width="1200" height="28" viewBox="0 0 1200 28" aria-hidden="true">
      <polygon points="508,28 537,0 866,0 837,28" fill="var(--purple)"/>
      <polygon points="848,28 877,0 1200,0 1200,28" fill="var(--purple)"/>
    </svg>
    <div class="cta-text cta-phone">Call to <span class="number">1300 642 917</span></div>
    <div class="cta-text cta-web">www.harbourvf.com.au</div>
  </div>
</body>
</html>
```